Professional/modern business card design for construction company

We need a new business card design, double sided keeping it modern, sleek, professional and simple. We are an earthmoving business but do not want any pictures of machinery. I would like one side to have the logo and the other to have all the information, keeping with the colors in our logo. The business card will need to be able to be customised so we can use it for several different managers., we would also like to be able to use the design to apply it to other stationary ie. letterheads, notebooks etc. We do not really have a tag line but we could put on there that we specialise in - Agriculture, Civil Construction and Mining.

Contact Information for Business Card

Balgo Groundworks Pty Ltd
ABN 58 402 917 364
82 Dunmore Creek Road, Narrabri NSW 2390

Desmond Fairweather
Managing Director
P 0438 614 205
E desfairweather@balgogroundworks.com.au

Font styles to use
Serif
Sans Serif

Requirements
Nice to have
• I have attached some examples of ideas.
Should not have
• images of machinery

```html
<!DOCTYPE html>
<html lang="en">
<head>
<meta charset="utf-8">
<title>Balgo Groundworks Business Card</title>
<link href="https://fonts.googleapis.com/css2?family=Montserrat:wght@700;800;900&family=Lato:wght@400;700&display=swap" rel="stylesheet">
<style>
  :root {
    --bg: #2a2a2a;
    --charcoal: #414141;
    --ink: #3a3a3a;
    --orange: #f48a1f;
    --white: #ffffff;
    --muted: #d9d9d9;
  }
  * { box-sizing: border-box; margin: 0; padding: 0; }
  html, body { width: 1200px; height: 895px; overflow: hidden; }
  body {
    background: var(--bg);
    display: flex;
    align-items: center;
    justify-content: center;
    gap: 40px;
    font-family: "Lato", sans-serif;
  }
  .card {
    position: relative;
    width: 540px;
    height: 330px;
    border-radius: 16px;
    overflow: hidden;
  }

  /* Front */
  .card--front {
    background: var(--charcoal);
    display: flex;
    align-items: center;
    justify-content: center;
  }
  .front-brand { text-align: left; }
  .front-brand__row { display: flex; align-items: center; gap: 12px; }
  .front-brand__mark { width: 20px; height: 20px; background: var(--orange); flex: none; }
  .front-brand__name {
    font-family: "Montserrat", sans-serif;
    font-weight: 800;
    font-size: 23px;
    line-height: 1.1;
    letter-spacing: 0.3px;
    color: var(--white);
    text-transform: uppercase;
    white-space: nowrap;
  }
  .front-brand__tagline {
    margin-top: 12px;
    padding-left: 32px;
    font-size: 14px;
    color: var(--muted);
    letter-spacing: 0.3px;
  }

  /* Back */
  .card--back { background: var(--white); }
  .back-strip { position: absolute; left: 0; bottom: 0; width: 540px; height: 60px; }
  .back-abn {
    position: absolute;
    right: 22px;
    bottom: 14px;
    font-family: "Montserrat", sans-serif;
    font-weight: 700;
    font-size: 14px;
    letter-spacing: 1px;
    color: var(--ink);
  }
  .back-brand {
    position: absolute;
    left: 24px;
    top: 132px;
    width: 215px;
  }
  .back-brand__row { display: flex; align-items: flex-start; gap: 9px; }
  .back-brand__mark { width: 14px; height: 14px; background: var(--orange); flex: none; margin-top: 3px; }
  .back-brand__name {
    font-family: "Montserrat", sans-serif;
    font-weight: 800;
    font-size: 17px;
    line-height: 1.2;
    color: var(--ink);
    text-transform: uppercase;
  }
  .back-divider {
    position: absolute;
    left: 244px;
    top: 40px;
    width: 1.5px;
    height: 200px;
    background: var(--ink);
  }
  .contact {
    position: absolute;
    left: 262px;
    top: 38px;
    width: 272px;
    color: var(--ink);
  }
  .contact__name {
    font-family: "Montserrat", sans-serif;
    font-weight: 900;
    font-size: 17px;
    text-transform: uppercase;
    letter-spacing: 0.2px;
    white-space: nowrap;
  }
  .contact__first { color: var(--orange); }
  .contact__title { font-size: 12.5px; margin-top: 2px; }
  .contact__address { font-size: 12.5px; line-height: 1.45; margin-top: 16px; }
  .contact__list { list-style: none; margin-top: 14px; font-size: 11.5px; }
  .contact__item { display: flex; align-items: center; gap: 8px; line-height: 1.75; white-space: nowrap; }
  .contact__icon { width: 12px; height: 12px; flex: none; }
  .contact__accent { color: var(--orange); }
</style>
</head>
<body>

  <section class="card card--front" aria-label="Card front">
    <div class="front-brand">
      <div class="front-brand__row">
        <span class="front-brand__mark"></span>
        <span class="front-brand__name">Balgo Groundworks Pty Ltd</span>
      </div>
      <p class="front-brand__tagline">Agriculture, Civil Construction and Mining</p>
    </div>
  </section>

  <section class="card card--back" aria-label="Card back">
    <svg class="back-strip" viewBox="0 0 540 60" aria-hidden="true">
      <polygon points="0,52 318,52 318,60 0,60" fill="#414141"/>
      <polygon points="318,12 540,12 540,60 310,60" fill="#f48a1f"/>
    </svg>
    <p class="back-abn">ABN 58 402 917 364</p>

    <div class="back-brand">
      <div class="back-brand__row">
        <span class="back-brand__mark"></span>
        <span class="back-brand__name">Balgo Groundworks<br>Pty Ltd</span>
      </div>
    </div>

    <div class="back-divider"></div>

    <div class="contact">
      <h1 class="contact__name"><span class="contact__first">Desmond</span> Fairweather</h1>
      <p class="contact__title">Managing Director</p>
      <p class="contact__address">82 Dunmore Creek Road<br>Wirralong NSW 2395</p>
      <ul class="contact__list">
        <li class="contact__item">
          <svg class="contact__icon" viewBox="0 0 12 12" aria-hidden="true"><rect x="3" y="0.8" width="6" height="10.4" rx="1.2" fill="none" stroke="#f48a1f" stroke-width="1.2"/><line x1="5" y1="9.3" x2="7" y2="9.3" stroke="#f48a1f" stroke-width="1"/></svg>
          <span>0438 614 205</span>
        </li>
        <li class="contact__item">
          <svg class="contact__icon" viewBox="0 0 12 12" aria-hidden="true"><rect x="0.8" y="2.5" width="10.4" height="7" fill="none" stroke="#f48a1f" stroke-width="1.2"/><polyline points="0.8,2.5 6,6.6 11.2,2.5" fill="none" stroke="#f48a1f" stroke-width="1.2"/></svg>
          <span>desfairweather@<span class="contact__accent">balgogroundworks</span>.com.au</span>
        </li>
        <li class="contact__item">
          <svg class="contact__icon" viewBox="0 0 12 12" aria-hidden="true"><circle cx="6" cy="6" r="5.2" fill="none" stroke="#f48a1f" stroke-width="1.1"/><ellipse cx="6" cy="6" rx="2.3" ry="5.2" fill="none" stroke="#f48a1f" stroke-width="1"/><line x1="0.8" y1="6" x2="11.2" y2="6" stroke="#f48a1f" stroke-width="1"/></svg>
          <span>www.<span class="contact__accent">balgogroundworks</span>.com.au</span>
        </li>
      </ul>
    </div>
  </section>

</body>
</html>
```